Wordpress template re-design of current website

We need a WordPress template design and new look for our existing website. Our existing site it located at www.velmoro.com.au We are a tech company and want a fresh, clean modern website that matches our brand, services and logo colors. Our main Services are hospitality solutions, Velmoro TV solution and managed networks, more information on these can come from our existing website.

Target Market(s)

We are a tech company so must have a modern feel for new technology

Industry/Entity Type

It Company

Number of Pages Required

5+ page

Font styles to use
Sans Serif

Requirements
Must have
• Be based on a wordpress templete design and match the services that we have in our existing website, in the testimonials want a place for video testimonials as well as text. Nice clean icons used for graphics to represent services.
Nice to have
• nice visual representation of our services in the way of clean icons etc
Should not have
• Clutter

```html
<!DOCTYPE html>
<html lang="en">
<head>
<meta charset="utf-8">
<title>Velmoro Wireless</title>
<link href="https://fonts.googleapis.com/css2?family=Roboto+Condensed:ital,wght@0,300;0,400;0,700;1,300&family=Roboto+Slab:wght@300;400;700&display=swap" rel="stylesheet">
<style>
:root{
  --navy:#0b3d7e;
  --navy-dark:#0a3469;
  --blue-text:#0f4a96;
  --grey-band:#6c7a86;
  --foot-grey:#efefef;
  --green:#1c9a4c;
  --teal:#1f8fa0;
  --slate:#6f7478;
  --olive:#a38f12;
  --ink:#333;
  --white:#fff;
}
*{margin:0;padding:0;box-sizing:border-box}
html,body{width:743px;height:1200px;overflow:hidden}
body{font-family:"Roboto Condensed",sans-serif;color:var(--ink);background:var(--white);position:relative}
.slab{font-family:"Roboto Slab",serif}

.topbar{position:absolute;top:0;left:0;width:743px;height:45px;background:var(--navy-dark);color:#fff;font-size:8px}
.topbar .contact{position:absolute;left:118px;top:8px;display:flex;gap:8px;align-items:center}
.topbar .contact span{display:flex;align-items:center;gap:3px}
.topbar .addr{position:absolute;right:165px;top:8px;color:#cfd8e6}
.topbar .social{position:absolute;right:118px;top:7px;display:flex;gap:5px}
.sq{width:11px;height:11px;background:#c9cfd8;display:block}

.hero{position:absolute;top:45px;left:0;width:743px;height:276px;background:linear-gradient(135deg,#2a5da6 0%,#1d4f99 45%,#15427f 100%)}
.hero-title{position:absolute;top:140px;width:743px;text-align:center;color:#fff;font-family:"Roboto Slab",serif;font-weight:300;font-size:24px}
.hero-text{position:absolute;top:181px;left:210px;width:323px;text-align:center;color:#e6ecf5;font-size:8.6px;line-height:12.5px}
.hero-btn{position:absolute;top:219px;left:350px;width:43px;height:15px;background:#6b7684;color:#fff;font-size:7px;text-align:center;line-height:15px}
.arrow{position:absolute;top:115px}

.header{position:absolute;top:25px;left:118px;width:507px;height:38px;background:#fff}
.logo{position:absolute;left:8px;top:8px;display:flex;align-items:center;gap:5px;color:var(--navy);font-weight:700;font-size:17px}
.logo i{width:10px;height:10px;border-radius:50%;background:var(--navy);display:block}
.nav{position:absolute;right:12px;top:12px;display:flex;gap:13px;font-size:7.4px;align-items:center}
.nav .on{color:var(--blue-text)}
.nav .portal{background:#6c7a86;color:#fff;padding:3px 7px}

.intro{position:absolute;top:346px;width:743px;text-align:center}
.h2{font-family:"Roboto Slab",serif;font-weight:400;font-size:20px;color:var(--navy)}
.sub{font-size:6.8px;color:var(--blue-text);margin-top:1px}
.lead{font-size:8.6px;line-height:11.5px;margin-top:8px;color:#333}

.tiles{position:absolute;top:424px;left:118px;width:507px;height:130px;display:flex;gap:1px}
.tile{flex:1;color:#fff;text-align:center;padding-top:22px}
.tile h3{font-family:"Roboto Slab",serif;font-size:11.4px;font-weight:700;margin-top:6px}
.tile p{font-size:7px;line-height:10.5px;margin-top:2px;padding:0 6px}
.t1{background:var(--green)}.t2{background:var(--teal)}.t3{background:var(--slate)}.t4{background:var(--olive)}

.band{position:absolute;top:591px;left:0;width:743px;height:110px;background:var(--navy);color:#fff;text-align:center;font-size:14.6px;line-height:22px;padding-top:31px;font-weight:400}

.clients{position:absolute;top:730px;width:743px;text-align:center}
.logos{position:absolute;top:810px;left:138px;width:470px;display:flex;justify-content:space-between;align-items:center;font-size:11px;font-weight:700;color:#333}
.logos span{display:flex;align-items:center;gap:4px}
.logos i{width:8px;height:8px;background:#e08a1e;display:block}

.testi{position:absolute;top:864px;left:0;width:743px;height:250px;background:var(--grey-band);color:#fff;text-align:center}
.testi .h2{color:#fff;margin-top:28px}
.testi .sub{color:#eef1f4}
.portrait{width:54px;height:47px;margin:14px auto 0;background:linear-gradient(160deg,#3b4a3a,#1d2320)}
.name{font-size:8.8px;margin-top:6px}
.quote{font-style:italic;font-weight:300;font-size:7.3px;line-height:11px;width:405px;margin:12px auto 0}
.dots{display:flex;gap:3px;justify-content:center;margin-top:12px}
.dots b{width:5px;height:5px;border-radius:50%;background:#fff;display:block}
.dots b.on{background:var(--navy);border:1px solid #fff}

.footnav{position:absolute;top:1114px;left:0;width:743px;height:27px;background:var(--navy);color:#fff;font-size:7.2px;display:flex;justify-content:center;align-items:center;gap:9px}
.footnav .sep{color:#7f9cc4}
.foot{position:absolute;top:1141px;left:0;width:743px;height:59px;background:var(--foot-grey);text-align:center}
.foot .line{margin-top:10px;font-size:7.3px;color:var(--blue-text);display:flex;justify-content:center;gap:6px;align-items:center}
.foot .sq{background:#3e6fbf;width:9px;height:9px}
.foot .copy{margin-top:13px;font-size:6.8px;color:#999}
</style>
</head>
<body>

<div class="hero" role="img" aria-label="Blue-tinted photo of a hotel bedroom"></div>
<svg class="arrow" style="left:44px" width="14" height="26" viewBox="0 0 14 26"><path d="M12 1 1 13l11 12" fill="none" stroke="#fff" stroke-width="1.5"/></svg>
<svg class="arrow" style="right:44px" width="14" height="26" viewBox="0 0 14 26"><path d="M2 1l11 12L2 25" fill="none" stroke="#fff" stroke-width="1.5"/></svg>
<div class="hero-title">Hospitality Solutions</div>
<div class="hero-text">Lorem ipsum dolor sit amet, consectetur adipisicing elit, sed do eiusmod tempor incididunt ut labore et dolore magna aliqua.</div>
<div class="hero-btn">Read More</div>

<div class="topbar">
  <div class="contact">
    <span><svg width="8" height="8" viewBox="0 0 10 10"><path d="M2 1l2 2-1 1.5c.6 1.2 1.3 1.9 2.5 2.5L7 6l2 2-1.3 1.3C4.5 9 1 5.5.7 2.3z" fill="#fff"/></svg>1300 555 214</span>
    <span style="color:#8ea4c6">|</span>
    <span><svg width="9" height="7" viewBox="0 0 9 7"><rect x=".5" y=".5" width="8" height="6" fill="none" stroke="#fff"/><path d="M.5.5l4 3 4-3" fill="none" stroke="#fff"/></svg>sales@velmoro.com.au</span>
  </div>
  <div class="addr">48 Harbour Crescent, Kingsford Lakes, QLD 4230</div>
  <div class="social"><i class="sq"></i><i class="sq"></i></div>
</div>

<header class="header">
  <div class="logo"><i></i>Velmoro</div>
  <nav class="nav">
    <span class="on">HOME</span><span>SERVICES</span><span>ABOUT</span><span>OUR WORK</span><span>CONTACT</span><span class="portal">PORTAL</span>
  </nav>
</header>

<section class="intro">
  <h2 class="h2">VELMORO WIRELESS</h2>
  <div class="sub">Creating solutions that work.</div>
  <p class="lead">Velmoro Wireless has been a leader in wireless networks and internet billing systems for over a decade.<br>Velmoro currently has completed over 2000 installations.</p>
</section>

<section class="tiles">
  <div class="tile t1">
    <svg width="34" height="34" viewBox="0 0 34 34" fill="none" stroke="#fff" stroke-width="1.4"><rect x="13" y="12" width="8" height="17" rx="3"/><circle cx="17" cy="21" r="1.5"/><path d="M10 8a10 10 0 0 0 0 14M24 8a10 10 0 0 1 0 14M7 5a14 14 0 0 0 0 20M27 5a14 14 0 0 1 0 20"/></svg>
    <h3>Wi-Fi Hotspots</h3><p>Leading supplier of public access and internet billing systems.</p>
  </div>
  <div class="tile t2">
    <svg width="34" height="34" viewBox="0 0 34 34" fill="none" stroke="#fff" stroke-width="1.4"><rect x="3" y="6" width="28" height="19"/><path d="M14 11v9l7-4.5z" fill="#fff"/><path d="M11 29h12"/></svg>
    <h3>Velmoro TV</h3><p>Turn you standard TV into a full guest information system and point</p>
  </div>
  <div class="tile t3">
    <svg width="34" height="34" viewBox="0 0 34 34" fill="none" stroke="#fff" stroke-width="1.4"><path d="M7 3h13l6 6v22H7z"/><rect x="13" y="16" width="16" height="11" rx="2"/><path d="M18 19v5M24 19v5M18 21.5h6"/></svg>
    <h3>HSIA Solutions</h3><p>Our guest acceess solutions have been built with the guest in mind and</p>
  </div>
  <div class="tile t4">
    <svg width="34" height="34" viewBox="0 0 34 34" fill="none" stroke="#fff" stroke-width="1.4"><circle cx="9" cy="18" r="5"/><circle cx="25" cy="8" r="5"/><circle cx="25" cy="27" r="5"/><path d="M13.5 15.5l7-5M13.5 20.5l7 4.5"/></svg>
    <h3>Social Wi-Fi</h3><p>Get more out of your existing Wi-Fi with our social plug-ins to gain</p>
  </div>
</section>

<section class="band">We strive to out work our competition with an effective approach and a powerful<br>skill set, which is why were industry leading.</section>

<section class="clients">
  <h2 class="h2">OUR CLIENTS</h2>
  <div class="sub">Solution for our happy clients</div>
  <p class="lead">Lorem ipsum dolor sit amet, consectetur adipisicing elit, sed do eiusmod tempor incididunt ut labore et dolore magna aliqua.<br>Ut enim ad minim veniam, quis nostrud exercitation ullamco laboris</p>
</section>
<div class="logos">
  <span>Tarrow Tours</span><span>Northvane</span><span><i></i>Staybrook</span><span>Hallmere</span><span>Roamly</span><span>Corvel Mining</span>
</div>

<section class="testi">
  <h2 class="h2">TESTIMONIALS</h2>
  <div class="sub">They Say Great Things</div>
  <div class="portrait" role="img" aria-label="Video testimonial thumbnail of the property manager"></div>
  <div class="name">Daniel Ashby - Property Manager</div>
  <p class="quote">Installing Velmoro Internet Solution has been a great investment for this business. The staff were very professional and easy to work with and gave us several options to consider that would work best for the business. The installation was easy and happened without any problems at all. The system is easy to use for both guests and staff, which can be tailored to suit the needs of the guest and business, which was a deciding factor. I would highly recommend Velmoro as you're in room internet solution</p>
  <div class="dots"><b></b><b></b><b class="on"></b><b></b></div>
</section>

<nav class="footnav"><span>Case Studies</span><span class="sep">|</span><span>Testimonials</span><span class="sep">|</span><span>News</span><span class="sep">|</span><span>Resellers</span></nav>
<footer class="foot">
  <div class="line"><span>48 Harbour Crescent, Kingsford Lakes, QLD 4230.</span><span>1300 555 214</span><span>sales@velmoro.com.au</span><i class="sq"></i><i class="sq"></i></div>
  <div class="copy">2015 Velmoro Wireless. All Rights Reserved.</div>
</footer>

</body>
</html>
```